Sunbeam Jam - Concert Poster

We need a poster for a concert involving 3 bands. Marzipod, Auntie's Pickles and Velveteen Ned. The event is called the Sunbeam Jam. The poster will be a take away. We plan to print some to give out and some for advertising. Should be something people will want to put up on a wall. The poster should have a psychedelic "flavor", colorful.
Info. that needs to be on the poster: Sunbeam Jam - Band Names - Barnaby Tuck's Music Hall - 4812 Route 17, Felton CA - $10 advance Tix - $12 at Door - for tickets www.barnabytucksmusic. - 21 and Over - March 21 2015 - Doors open at 7:00.

```html
<!DOCTYPE html>
<html lang="en">
<head>
<meta charset="utf-8">
<title>Sunbeam Jam – Concert Poster</title>
<link rel="stylesheet" href="https://fonts.googleapis.com/css2?family=Permanent+Marker&family=Archivo:wght@600;700&display=swap">
<style>
  :root {
    --purple: #7a0a7e;
    --green: #2fe01c;
    --red: #ff3b2a;
    --white: #ffffff;
    --brush: "Permanent Marker", cursive;
    --sans: "Archivo", sans-serif;
  }
  html, body {
    margin: 0;
    padding: 0;
    width: 776px;
    height: 1200px;
    overflow: hidden;
    background: var(--purple);
  }
  .poster {
    position: relative;
    width: 776px;
    height: 1200px;
    overflow: hidden;
    background: var(--purple);
  }
  .poster svg { display: block; }
  .swirl { fill: var(--red); }
  .brush-block { fill: var(--green); }
  .band-name {
    font-family: var(--brush);
    font-size: 74px;
    fill: var(--white);
    text-transform: uppercase;
  }
  .event-date {
    font-family: var(--sans);
    font-weight: 600;
    font-size: 38px;
    letter-spacing: 5px;
    fill: var(--white);
  }
  .doors {
    font-family: var(--sans);
    font-weight: 600;
    font-size: 27px;
    letter-spacing: 3px;
    fill: var(--white);
  }
  .event-title {
    font-family: var(--brush);
    font-size: 200px;
    fill: var(--white);
    text-transform: uppercase;
  }
  .info-line {
    font-family: var(--sans);
    font-weight: 700;
    font-size: 22px;
    letter-spacing: 2.5px;
    fill: var(--white);
  }
  .age-limit {
    font-family: var(--sans);
    font-weight: 700;
    font-size: 26px;
    letter-spacing: 2.5px;
    fill: var(--white);
  }
  .ticket-call {
    font-family: var(--brush);
    font-size: 36px;
    fill: var(--white);
    text-transform: uppercase;
  }
  .ticket-url {
    font-family: var(--brush);
    font-size: 38px;
    fill: var(--white);
    text-transform: uppercase;
    letter-spacing: 3px;
  }
</style>
</head>
<body>
<main class="poster">
  <svg width="776" height="1200" viewBox="0 0 776 1200" xmlns="http://www.w3.org/2000/svg">
    <!-- red flowing swirls -->
    <g role="img" aria-label="Flowing red psychedelic swirl shapes">
      <path class="swirl" d="M150 0 H205 C195 30 180 55 160 70 C150 45 148 20 150 0 Z"/>
      <path class="swirl" d="M590 290 C640 320 660 380 640 440 C625 500 670 560 660 640 C650 720 690 790 660 880 L600 880 C620 800 585 730 600 650 C612 570 570 520 585 450 C598 390 560 340 590 290 Z"/>
      <path class="swirl" d="M0 930 C60 900 150 880 210 910 C240 980 180 1020 200 1080 C215 1130 190 1170 220 1200 H0 Z"/>
      <path class="swirl" d="M600 1110 C650 1080 720 1090 776 1070 V1200 H610 C640 1170 590 1140 600 1110 Z"/>
      <path class="swirl" d="M150 440 C170 520 140 600 165 680 C180 720 160 760 175 800 L150 800 C135 740 150 680 130 610 C120 550 140 490 150 440 Z"/>
    </g>
    <!-- green brush blocks -->
    <g role="img" aria-label="Bright green painted brush strokes">
      <path class="brush-block" d="M118 62 C250 50 450 48 640 58 L645 350 C560 330 480 345 420 360 C360 380 300 340 250 400 C220 440 180 470 160 480 L130 470 C125 330 112 200 118 62 Z"/>
      <path class="brush-block" d="M230 520 C300 440 420 400 540 410 C600 415 630 440 640 470 C590 455 520 450 450 470 C360 500 290 560 240 600 Z"/>
      <path class="brush-block" d="M165 880 C220 860 300 880 420 860 C470 850 510 830 560 840 C600 850 630 880 650 895 L650 1040 C690 1050 705 1080 690 1120 C520 1135 330 1130 140 1140 C135 1110 140 1080 150 1060 L165 1060 C160 1000 165 940 165 880 Z"/>
    </g>

    <!-- band line-up -->
    <text class="band-name" x="140" y="140" textLength="500" lengthAdjust="spacingAndGlyphs">Marzipod</text>
    <text class="band-name" x="140" y="220" textLength="500" lengthAdjust="spacingAndGlyphs">Auntie's Pickles</text>
    <text class="band-name" x="140" y="300" textLength="495" lengthAdjust="spacingAndGlyphs">Velveteen Ned</text>

    <!-- date and doors -->
    <text class="event-date" x="186" y="395" textLength="390" lengthAdjust="spacingAndGlyphs">MARCH 21 2015</text>
    <text class="doors" x="186" y="438" textLength="390" lengthAdjust="spacingAndGlyphs">DOORS OPEN 7:00pm</text>

    <!-- event title -->
    <text class="event-title" x="150" y="640" textLength="500" lengthAdjust="spacingAndGlyphs" transform="rotate(-3 400 560)">Sunbeam</text>
    <text class="event-title" x="180" y="860" textLength="440" lengthAdjust="spacingAndGlyphs" font-size="230" transform="rotate(2 400 780)">Jam</text>

    <!-- venue details -->
    <text class="info-line" x="178" y="900" textLength="390" lengthAdjust="spacingAndGlyphs">$10 ADVANCE TIX/$12 AT DOOR</text>
    <text class="info-line" x="178" y="948" textLength="390" lengthAdjust="spacingAndGlyphs">BARNABY TUCK'S MUSIC HALL</text>
    <text class="info-line" x="178" y="995" textLength="390" lengthAdjust="spacingAndGlyphs">4812 ROUTE 17, FELTON CA</text>
    <text class="age-limit" x="176" y="1050" textLength="222" lengthAdjust="spacingAndGlyphs">21 AND OVER</text>
    <text class="ticket-call" x="425" y="1045" textLength="225" lengthAdjust="spacingAndGlyphs" transform="rotate(-3 535 1035)">For Tickets:</text>
    <text class="ticket-url" x="150" y="1112" textLength="490" lengthAdjust="spacingAndGlyphs" transform="rotate(-2 395 1100)">www.barnabytucksmusic.com</text>
  </svg>
</main>
</body>
</html>
```